TVQ-Business Card Design

I need a modern, professional business card design that includes my logo as the main feature, maybe the entire background with the contact info overlaying or even contact info on the back and the logo full frontal

Neat and organized placement of contact information

Would like to see options in black and white

Target Market(s)

real estate Developers, Construction managers, business and home owners

Industry/Entity Type

Construction

Contact Information for Business Card

TVQ Construction
Dennis Fairweather
General Contractor

Office: 1-888-902-7351 Ext #1
Cell: 412-730-2168
Fax: 1-888-902-7351

Font styles to use
Serif

Requirements
Must have
• title
• office #
• cell #
• Email
• website
Nice to have
• fax

```html
<!DOCTYPE html>
<html lang="en">
<head>
<meta charset="utf-8">
<title>TVQ Construction – Business Card</title>
<link rel="stylesheet" href="https://fonts.googleapis.com/css2?family=Open+Sans:wght@400;600&display=swap">
<style>
  :root {
    --backdrop: #e4e4e2;
    --card-white: #f7f7f5;
    --card-black: #1a1a1a;
    --brand-green: #3f9a2c;
    --brand-green-light: #5cbf3c;
    --ink: #2b2b2b;
    --ink-soft: #555;
  }
  * { box-sizing: border-box; margin: 0; padding: 0; }
  html, body {
    width: 1200px; height: 844px; overflow: hidden;
    background: var(--backdrop);
    font-family: "Open Sans", Arial, sans-serif;
  }
  .stage {
    position: relative; width: 1200px; height: 844px;
  }
  .card {
    position: absolute; top: 272px;
    width: 525px; height: 300px;
    box-shadow: 0 10px 24px rgba(0,0,0,.18);
  }
  .card--front { left: 50px; background: var(--card-white); }
  .card--back  { left: 625px; background: var(--card-black); }

  /* brand name set in text font */
  .brand {
    position: absolute; display: flex; align-items: center; gap: 10px;
    color: var(--brand-green); font-weight: 600;
  }
  .brand__mark { background: var(--brand-green); display: block; }
  .card--front .brand { right: 34px; top: 52px; font-size: 30px; }
  .card--front .brand__mark { width: 16px; height: 16px; }
  .card--back .brand {
    left: 0; right: 0; top: 118px; justify-content: center;
    font-size: 40px; color: var(--brand-green-light);
  }
  .card--back .brand__mark { width: 20px; height: 20px; background: var(--brand-green-light); }

  .rule {
    position: absolute; left: 0; right: 0; height: 1.5px;
    background: var(--brand-green);
  }
  .rule--upper { top: 150px; }
  .rule--lower { top: 262px; }

  .person { position: absolute; left: 30px; top: 166px; }
  .person__name { color: var(--brand-green); font-weight: 600; font-size: 19px; line-height: 1.2; }
  .person__title { color: var(--ink); font-size: 13px; margin-top: 2px; }

  .contact {
    position: absolute; display: flex; align-items: center; gap: 6px;
    color: var(--ink); font-size: 13px; white-space: nowrap;
  }
  .contact svg { width: 12px; height: 12px; fill: var(--brand-green); flex: none; }
  .contact--cell    { left: 262px; top: 168px; }
  .contact--fax     { left: 390px; top: 168px; }
  .contact--office  { left: 30px;  top: 232px; }
  .contact--web     { left: 212px; top: 232px; }
  .contact--email   { left: 30px;  top: 272px; }
</style>
</head>
<body>
<main class="stage">
  <section class="card card--front" aria-label="Business card front">
    <div class="brand"><span class="brand__mark"></span>TVQ Construction</div>
    <div class="rule rule--upper"></div>

    <div class="person">
      <p class="person__name">Dennis Fairweather</p>
      <p class="person__title">General Contractor</p>
    </div>

    <p class="contact contact--cell">
      <svg viewBox="0 0 12 12" aria-hidden="true"><path d="M3 0h6a1 1 0 0 1 1 1v10a1 1 0 0 1-1 1H3a1 1 0 0 1-1-1V1a1 1 0 0 1 1-1zm0 2v7h6V2z"/></svg>
      412-730-2168
    </p>
    <p class="contact contact--fax">
      <svg viewBox="0 0 12 12" aria-hidden="true"><path d="M3 0h6v3H3zM1 4h10a1 1 0 0 1 1 1v4h-2v3H2V9H0V5a1 1 0 0 1 1-1zm2 4v3h6V8z"/></svg>
      1-888-902-7351
    </p>
    <p class="contact contact--office">
      <svg viewBox="0 0 12 12" aria-hidden="true"><path d="M2.5 0.5l2 2.5-1.2 1.3a7 7 0 0 0 4.4 4.4L9 7.5l2.5 2-1.5 2C5 11.5.5 7 .5 2z"/></svg>
      1-888-902-7351 Ext #1
    </p>
    <p class="contact contact--web">
      <svg viewBox="0 0 12 12" aria-hidden="true"><circle cx="6" cy="6" r="6"/></svg>
      www.tvqbuild.com
    </p>
    <div class="rule rule--lower"></div>
    <p class="contact contact--email">
      <svg viewBox="0 0 12 12" aria-hidden="true"><path d="M0 2h12v8H0zm1 1l5 3.5L11 3z"/></svg>
      info@tvqbuild.com
    </p>
  </section>

  <section class="card card--back" aria-label="Business card back">
    <div class="brand"><span class="brand__mark"></span>TVQ Construction</div>
  </section>
</main>
</body>
</html>
```